new business card for plan-go-NET.com CEO

business card showing personal detail + logo on front and (larger size) logo on back

don't know what else to say to make up the 300 words don't know what else to say to make up the 300 words don't know what else to say to make up the 300 words don't know what else to say to make up the 300 words don't know what else to say to make up the 300 words don't know what else to say to make up the 300 words don't know what else to say to make up the 300 words don't know what else to say to make up the 300 words don't know what else to say to make up the 300 words don't know what else to say to make up the 300 words don't know what else to say to make up the 300 words don't know what else to say to make up the 300 words don't know what else to say to make up the 300 words don't know what else to say to make up the 300 words don't know what else to say to make up the 300 words don't know what else to say to make up the 300 words don't know what else to say to make up the 300 words don't know what else to say to make up the 300 words

Target Market(s)

Utilities & Telcos

Industry/Entity Type

It Company

Contact Information for Business Card

Dr Conrad Pilsby
Group Managing Director
plan-go-NET
L9/415 Marlow Street
Melbourne VIC 3000
AUSTRALIA
+61-3-7294-5182
cpilsby@plan-go-NET.com
www.plan-go-NET.com

Colors
0255a3

Requirements
Must have
• http://www.plan-go-net.com/wp-content/uploads/2017/02/new-plan-go-NET-logo-2.png on the back of the business card

```html
<!DOCTYPE html>
<html lang="en">
<head>
<meta charset="utf-8">
<title>plan-go-NET business card</title>
<link href="https://fonts.googleapis.com/css2?family=Montserrat:wght@400;500;600&display=swap" rel="stylesheet">
<style>
  :root {
    --stage: #3a3a3c;
    --paper: #ffffff;
    --brand-blue: #243f8f;
    --brand-navy: #212d5e;
    --ink-blue: #2a3d91;
    --ink-grey: #3a3a3a;
  }
  html, body {
    margin: 0;
    width: 1200px;
    height: 1000px;
    overflow: hidden;
    background: var(--stage);
    font-family: "Montserrat", sans-serif;
  }
  .card {
    position: absolute;
    left: 277px;
    width: 646px;
    height: 379px;
    background: var(--paper);
    overflow: hidden;
  }
  .card--back { top: 87px; }
  .card--front { top: 534px; }
  .accent-area {
    position: absolute;
    background: linear-gradient(135deg, var(--brand-navy), var(--brand-blue));
  }
  .card--back .accent-area--top {
    left: 0;
    top: 0;
    width: 170px;
    height: 140px;
  }
  .card--back .accent-area--bottom {
    right: 0;
    bottom: 0;
    width: 166px;
    height: 165px;
  }
  .card--front .accent-area--side {
    right: 0;
    top: 0;
    width: 210px;
    height: 379px;
  }
  .wordmark {
    position: absolute;
    margin: 0;
    font-weight: 600;
    color: var(--ink-blue);
    white-space: nowrap;
    letter-spacing: -0.5px;
  }
  .card--back .wordmark {
    left: 0;
    width: 646px;
    text-align: center;
    top: 154px;
    font-size: 46px;
    line-height: 1;
  }
  .card--front .wordmark {
    left: 50px;
    top: 47px;
    font-size: 34px;
    line-height: 1;
  }
  .contact {
    position: absolute;
    left: 52px;
    top: 0;
    color: var(--ink-blue);
  }
  .contact__name {
    position: absolute;
    top: 116px;
    margin: 0;
    font-size: 27px;
    font-weight: 500;
    white-space: nowrap;
  }
  .contact__role {
    position: absolute;
    top: 150px;
    margin: 0;
    font-size: 16px;
    font-weight: 500;
    color: var(--ink-grey);
    white-space: nowrap;
  }
  .contact__block {
    position: absolute;
    margin: 0;
    font-style: normal;
    font-size: 16px;
    font-weight: 500;
    line-height: 20.5px;
    white-space: nowrap;
  }
  .contact__address { top: 185px; }
  .contact__lines { top: 266px; }
</style>
</head>
<body>

<section class="card card--back" aria-label="Card back">
  <div class="accent-area accent-area--top" role="img" aria-label="Decorative blue corner artwork"></div>
  <div class="accent-area accent-area--bottom" role="img" aria-label="Decorative blue corner artwork"></div>
  <p class="wordmark">plan-go-NET</p>
</section>

<section class="card card--front" aria-label="Card front">
  <div class="accent-area accent-area--side" role="img" aria-label="Decorative blue side artwork"></div>
  <p class="wordmark">plan-go-NET</p>
  <div class="contact">
    <h1 class="contact__name">Dr Conrad Pilsby</h1>
    <p class="contact__role">Group Managing Director</p>
    <address class="contact__block contact__address">
      L9/415 Marlow Street<br>
      Melbourne VIC 3000<br>
      AUSTRALIA
    </address>
    <p class="contact__block contact__lines">
      +61-3-7294-5182<br>
      cpilsby@plan-go-NET.com<br>
      www.plan-go-NET.com
    </p>
  </div>
</section>

</body>
</html>
```